Business cards and letterhead
Business cards and letterhead - Pharmacy/Pharmaceuticals
Creative Brief
Professional
Owen Lilcroft
Partner
4178 Heron Lake Road Suite 410 Grapevine, TX 76099
owen@torvalepz.com
torvalepz.com

```html
<!DOCTYPE html>
<html lang="en">
<head>
<meta charset="utf-8">
<title>Torvale Business Card</title>
<link rel="stylesheet" href="https://fonts.googleapis.com/css2?family=Open+Sans:wght@400;600;700&display=swap">
<style>
  :root {
    --page-bg: #e9ecef;
    --brand-blue: #1a6fc4;
    --brand-blue-deep: #0d4f9a;
    --brand-blue-light: #3d93e0;
    --card-white: #ffffff;
    --ink-blue: #1d5fa8;
    --ink-grey: #6a7480;
  }
  html, body {
    margin: 0;
    padding: 0;
    width: 1200px;
    height: 901px;
    overflow: hidden;
    background: var(--page-bg);
    font-family: "Open Sans", Arial, sans-serif;
  }
  .canvas {
    position: relative;
    width: 1200px;
    height: 901px;
  }
  .card {
    position: absolute;
    left: 250px;
    width: 700px;
    height: 400px;
    border-radius: 18px;
    overflow: hidden;
    box-shadow: 0 6px 18px rgba(0,0,0,0.18);
  }
  /* Back side */
  .card-back {
    top: 36px;
    background: linear-gradient(135deg, var(--brand-blue-light) 0%, var(--brand-blue) 50%, var(--brand-blue-deep) 100%);
    display: flex;
    align-items: center;
    justify-content: center;
  }
  .back-mark {
    display: flex;
    align-items: center;
    gap: 14px;
    color: var(--card-white);
    font-weight: 700;
    font-size: 40px;
  }
  .mark-dot {
    width: 40px;
    height: 40px;
    border-radius: 50%;
    background: var(--card-white);
  }
  /* Front side */
  .card-front {
    top: 466px;
    background: var(--card-white);
  }
  .front-waves {
    position: absolute;
    inset: 0;
  }
  .front-brand {
    position: absolute;
    top: 52px;
    left: 300px;
    display: flex;
    align-items: center;
    gap: 12px;
    color: var(--ink-blue);
    font-weight: 700;
    font-size: 42px;
  }
  .front-brand .mark-dot {
    width: 44px;
    height: 44px;
    background: var(--ink-blue);
  }
  .holder {
    position: absolute;
    left: 40px;
    top: 192px;
  }
  .holder-name {
    margin: 0;
    color: var(--ink-blue);
    font-weight: 600;
    font-size: 21px;
  }
  .holder-role {
    margin: 2px 0 0;
    color: var(--ink-grey);
    font-size: 13px;
  }
  .contact {
    position: absolute;
    right: 26px;
    top: 186px;
    text-align: right;
    color: var(--card-white);
    font-size: 13px;
    line-height: 17px;
  }
  .contact address {
    font-style: normal;
    margin-bottom: 10px;
  }
  .contact-row {
    display: flex;
    justify-content: flex-end;
    align-items: center;
    gap: 8px;
  }
  .contact-row svg {
    width: 11px;
    height: 11px;
    fill: var(--card-white);
  }
</style>
</head>
<body>
<main class="canvas">
  <section class="card card-back" aria-label="Card back">
    <div class="back-mark"><span class="mark-dot"></span>Torvale</div>
  </section>

  <section class="card card-front" aria-label="Card front">
    <svg class="front-waves" viewBox="0 0 700 400" preserveAspectRatio="none" aria-hidden="true">
      <defs>
        <linearGradient id="waveBlue" x1="0" y1="1" x2="1" y2="0">
          <stop offset="0" stop-color="#0d4f9a"/>
          <stop offset="1" stop-color="#3d93e0"/>
        </linearGradient>
      </defs>
      <path d="M470 0 C560 20 630 60 700 100 L700 0 Z" fill="url(#waveBlue)"/>
      <path d="M440 0 C540 25 620 70 700 118" fill="none" stroke="#1a6fc4" stroke-width="2"/>
      <path d="M0 400 L0 330 C150 320 300 260 420 200 C520 150 610 140 700 150 L700 400 Z" fill="url(#waveBlue)"/>
      <path d="M0 318 C160 308 300 250 420 190 C520 140 610 128 700 138" fill="none" stroke="#1a6fc4" stroke-width="3"/>
      <path d="M0 345 C170 335 320 270 440 212 C530 168 620 158 700 165" fill="none" stroke="#ffffff" stroke-width="2" opacity="0.7"/>
    </svg>

    <div class="front-brand"><span class="mark-dot"></span>Torvale</div>

    <div class="holder">
      <p class="holder-name">Owen Lilcroft</p>
      <p class="holder-role">Partner</p>
    </div>

    <div class="contact">
      <address>4178 Heron Lake Road<br>Suite 410<br>Grapevine, TX 76099</address>
      <div class="contact-row">2145550173<svg viewBox="0 0 12 12"><path d="M2 1h3l1 3-2 1a7 7 0 0 0 3 3l1-2 3 1v3a1 1 0 0 1-1 1A10 10 0 0 1 1 2a1 1 0 0 1 1-1z"/></svg></div>
      <div class="contact-row">2145550128<svg viewBox="0 0 12 12"><rect x="3" y="0.5" width="6" height="11" rx="1"/></svg></div>
      <div class="contact-row">2145550194<svg viewBox="0 0 12 12"><rect x="1" y="4" width="10" height="7" rx="1"/><rect x="3" y="1" width="6" height="3"/></svg></div>
      <div class="contact-row">2145550146<svg viewBox="0 0 12 12"><rect x="1" y="3" width="10" height="8" rx="1"/></svg></div>
      <div class="contact-row">owen@torvalepz.com<svg viewBox="0 0 12 12"><path d="M1 3h10v7H1z M1 3l5 4 5-4"/></svg></div>
      <div class="contact-row">torvalepz.com<svg viewBox="0 0 12 12"><circle cx="6" cy="6" r="5"/></svg></div>
    </div>
  </section>
</main>
</body>
</html>
```